Business Card Design

A card that's appealing to realtors and home buyers..
Something that's memorable,attractive, yet simple.

Home Inspection business.
Name of co. Birchwell Home Inspections
Serving Kern, Los Angeles, Santa Barbara & Ventura counties
NRQB Certified Inspectors (Use NRQB certified logo)
http://nrqb-example.com/logos/newlogos/NRQB_Logo008.gif
Mark Ollivane
555 314-2760
Gavin Ollivane
555 492-1835
Email :birchwellinspections@mailbox-example.com
Also use slogan: Providing peace of mind

```html
<!DOCTYPE html>
<html lang="en">
<head>
<meta charset="utf-8">
<title>Birchwell Home Inspections – Business Card</title>
<link rel="stylesheet" href="https://fonts.googleapis.com/css2?family=Oswald:wght@600&family=Open+Sans:wght@400&family=Alegreya:wght@400&display=swap">
<style>
  :root {
    --brand-red: #e0202e;
    --ink: #000000;
    --paper: #ffffff;
  }
  * { margin: 0; padding: 0; box-sizing: border-box; }
  html, body { width: 1200px; height: 702px; overflow: hidden; background: var(--paper); }
  .card {
    position: relative;
    width: 1200px;
    height: 702px;
    background: var(--paper);
    font-family: "Open Sans", Arial, sans-serif;
  }
  .company-name {
    position: absolute;
    top: 74px;
    left: 0;
    width: 1210px;
    text-align: center;
    font-family: "Oswald", "Arial Narrow", sans-serif;
    font-weight: 600;
    font-size: 68px;
    line-height: 1;
    color: var(--brand-red);
    letter-spacing: 0.5px;
  }
  .title-rule {
    position: absolute;
    top: 168px;
    left: 144px;
    width: 922px;
    height: 4px;
    background: var(--ink);
  }
  .service-area {
    position: absolute;
    top: 186px;
    left: 0;
    width: 1208px;
    text-align: center;
    font-size: 24px;
    color: var(--ink);
  }
  .slogan {
    position: absolute;
    top: 282px;
    left: 104px;
    font-family: "Alegreya", Georgia, serif;
    font-size: 57px;
    line-height: 1.1;
    color: var(--brand-red);
  }
  .contact-band {
    position: absolute;
    top: 415px;
    left: 0;
    width: 1200px;
    height: 287px;
    background: var(--ink);
  }
  .certification-badge {
    position: absolute;
    top: 280px;
    left: 862px;
    width: 194px;
    height: 208px;
  }
  .inspector {
    position: absolute;
    top: 462px;
  }
  .inspector--senior { left: 55px; }
  .inspector--junior { left: 483px; }
  .inspector-name {
    font-size: 36px;
    line-height: 1.2;
    color: var(--paper);
  }
  .inspector-phone {
    font-size: 27px;
    line-height: 1.2;
    color: var(--brand-red);
  }
  .email {
    position: absolute;
    top: 604px;
    left: 55px;
    color: var(--paper);
    font-size: 27px;
  }
  .email-label {
    color: var(--brand-red);
    font-size: 35px;
  }
</style>
</head>
<body>
  <div class="card">
    <h1 class="company-name">Birchwell Home Inspections</h1>
    <div class="title-rule"></div>
    <p class="service-area">Serving Kern, Los Angeles, Santa Barbara &amp; Ventura counties</p>
    <p class="slogan">Providing peace of mind</p>

    <div class="contact-band"></div>

    <svg class="certification-badge" viewBox="0 0 194 208" role="img" aria-label="NRQB certification badge">
      <rect x="0" y="0" width="194" height="208" fill="#ffffff"/>
      <rect x="12" y="12" width="170" height="184" fill="none" stroke="#000000" stroke-width="4"/>
    </svg>

    <div class="inspector inspector--senior">
      <p class="inspector-name">Mark Ollivane</p>
      <p class="inspector-phone">555 314-2760</p>
    </div>
    <div class="inspector inspector--junior">
      <p class="inspector-name">Gavin Ollivane</p>
      <p class="inspector-phone">555 492-1835</p>
    </div>

    <p class="email"><span class="email-label">Email:</span> birchwellinspections@mailbox-example.com</p>
  </div>
</body>
</html>
```